Harborline Network Advisors (HNA) Business Card

Front Side, add Company Logo
1.) Harborline Network Advisors
Director of Operations
Delgado, Marco T
(323) 555 0148
782 n Alder Ave Suite 300 PMB2093
Los Angeles, CA 90013
Marco@HarborlineNA.example
www.HarborlineNA.example
2.) Veteran-Owned Business (with Small EGA)

Back Side
- Pictures are ideas of what you can add. The description is what HNA does.
1.) Business Partners:
- Corvalis Business
- KX&L Business
- Tellmora Business
2.) What we do
- Broker of Internet service (partners above)
- Project Management/ Contract Management
- Government Contracts

```html
<!DOCTYPE html>
<html lang="en">
<head>
<meta charset="utf-8">
<title>Harborline Network Advisors – Business Card</title>
<link rel="stylesheet" href="https://fonts.googleapis.com/css2?family=Exo+2:ital,wght@0,400;0,500;0,600;0,700;0,800;1,700&display=swap">
<style>
  :root {
    --bg: #e9e6e1;
    --card-dark: #231f20;
    --bar-dark: #1c1a1b;
    --bar-mid: #3a3738;
    --yellow: #f6b91a;
    --grey-stripe: #d9d9d9;
    --white: #ffffff;
    --ink: #1d1d1f;
  }
  * { box-sizing: border-box; margin: 0; padding: 0; }
  html, body { width: 1200px; height: 992px; overflow: hidden; }
  body {
    background: var(--bg);
    font-family: "Exo 2", sans-serif;
    position: relative;
  }
  .card {
    position: absolute;
    left: 200px;
    width: 800px;
    height: 457px;
    border-radius: 26px;
    overflow: hidden;
    box-shadow: 0 6px 18px rgba(0,0,0,.18);
  }

  /* ---------- Back side ---------- */
  .card-back { top: 24px; background: var(--white); }
  .section-bar {
    position: absolute;
    left: 24px; right: 24px;
    height: 44px;
    border-radius: 10px;
    background: linear-gradient(180deg, var(--bar-mid), var(--bar-dark));
    display: flex; align-items: center; justify-content: center;
    color: var(--yellow);
    font-weight: 800; font-size: 24px; letter-spacing: 1px;
    text-transform: uppercase;
  }
  .section-bar .bullet {
    width: 16px; height: 16px; border-radius: 50%;
    background: var(--white); margin-right: 12px;
  }
  .bar-partners { top: 20px; }
  .bar-services { top: 180px; }
  .partners {
    position: absolute; top: 72px; left: 24px; right: 24px; height: 100px;
    display: flex; justify-content: space-around; align-items: center;
  }
  .partner {
    display: flex; align-items: center; gap: 10px;
    font-size: 24px; font-weight: 600; color: var(--ink);
  }
  .partner .dot { width: 22px; height: 22px; border-radius: 50%; background: var(--ink); }
  .services {
    position: absolute; top: 236px; left: 24px; right: 24px; height: 198px;
    display: flex; gap: 10px;
  }
  .service {
    flex: 1; position: relative; border-radius: 10px; overflow: hidden;
    display: flex; align-items: flex-end; justify-content: center;
    padding-bottom: 22px;
  }
  .service-photo { position: absolute; inset: 0; }
  .photo-datacenter { background: linear-gradient(135deg, #3b3a2c, #6b6a4a 45%, #9aa1a6); }
  .photo-fiber { background: linear-gradient(135deg, #2b2e2c, #3d8a3f 45%, #c9cfcf); }
  .photo-cabling { background: linear-gradient(135deg, #1f1f1f, #4a4a47 50%, #8a8b88); }
  .service-label {
    position: relative; text-align: center;
    color: var(--yellow); font-weight: 700; font-size: 20px; line-height: 1.1;
    text-transform: uppercase; text-shadow: 0 1px 3px rgba(0,0,0,.8);
  }

  /* ---------- Front side ---------- */
  .card-front { top: 511px; background: var(--card-dark); color: var(--white); }
  .veteran-badge {
    position: absolute; left: 46px; top: 34px;
    display: flex; align-items: center; gap: 12px;
  }
  .veteran-badge .seal { width: 46px; height: 46px; border-radius: 50%; background: #cfcfcf; }
  .veteran-badge .title { font-size: 28px; font-weight: 800; line-height: 1; letter-spacing: 1px; }
  .veteran-badge .sub { font-size: 14px; font-weight: 500; letter-spacing: .5px; }
  .contact-name {
    position: absolute; left: 46px; top: 128px;
    font-size: 52px; font-weight: 700; color: var(--yellow); letter-spacing: 1px;
  }
  .contact-role { position: absolute; left: 46px; top: 196px; font-size: 24px; font-weight: 500; }
  .rule { position: absolute; height: 2px; background: var(--yellow); }
  .rule-name { left: 46px; top: 238px; width: 714px; }
  .contact-list { position: absolute; left: 46px; top: 256px; list-style: none; }
  .contact-list li {
    display: flex; align-items: center; gap: 12px;
    font-size: 21px; line-height: 34px;
  }
  .contact-list svg { width: 18px; height: 18px; fill: var(--yellow); }
  .address {
    position: absolute; right: 40px; top: 258px; text-align: right;
    font-size: 21px; line-height: 30px;
  }
  .brand-mark {
    position: absolute; right: 40px; top: 40px; width: 230px;
    display: flex; flex-direction: column; align-items: center; gap: 14px;
  }
  .brand-mark .ring { width: 64px; height: 64px; border-radius: 50%; border: 3px solid var(--yellow); }
  .brand-mark .name {
    color: var(--yellow); font-weight: 700; font-size: 22px;
    text-align: center; text-transform: uppercase; letter-spacing: 2px; line-height: 1.25;
  }
  .footer-band { position: absolute; left: 0; bottom: 0; width: 800px; height: 96px; }
  .website {
    position: absolute; right: 40px; bottom: 14px;
    color: var(--ink); font-weight: 800; font-size: 24px; letter-spacing: 1px;
    text-transform: uppercase;
  }
</style>
</head>
<body>

  <section class="card card-back" aria-label="Business card back">
    <div class="section-bar bar-partners"><span class="bullet"></span>Business Partners</div>
    <div class="partners">
      <div class="partner"><span class="dot"></span>Corvalis Business</div>
      <div class="partner"><span class="dot"></span>KX&amp;L Business</div>
      <div class="partner"><span class="dot"></span>Tellmora Business</div>
    </div>
    <div class="section-bar bar-services"><span class="bullet"></span>What We Do</div>
    <div class="services">
      <div class="service">
        <div class="service-photo photo-datacenter" role="img" aria-label="Photo of a data center server aisle"></div>
        <p class="service-label">Broker of Internet<br>Service</p>
      </div>
      <div class="service">
        <div class="service-photo photo-fiber" role="img" aria-label="Photo of a fiber patch panel with green connectors"></div>
        <p class="service-label">Project / Contract<br>Management</p>
      </div>
      <div class="service">
        <div class="service-photo photo-cabling" role="img" aria-label="Photo of network equipment with cabling"></div>
        <p class="service-label">Government<br>Contracts</p>
      </div>
    </div>
  </section>

  <section class="card card-front" aria-label="Business card front">
    <div class="veteran-badge">
      <span class="seal"></span>
      <div>
        <div class="title">VETERAN</div>
        <div class="sub">OWNED BUSINESS</div>
      </div>
    </div>

    <div class="brand-mark">
      <span class="ring"></span>
      <span class="name">Harborline<br>Network Advisors</span>
    </div>

    <h1 class="contact-name">DELGADO MARCO T</h1>
    <p class="contact-role">Director of Operations</p>
    <div class="rule rule-name"></div>

    <ul class="contact-list">
      <li>
        <svg viewBox="0 0 24 24" aria-hidden="true"><path d="M6.6 10.8a15.1 15.1 0 0 0 6.6 6.6l2.2-2.2a1 1 0 0 1 1-.25 11.4 11.4 0 0 0 3.6.57 1 1 0 0 1 1 1V20a1 1 0 0 1-1 1A17 17 0 0 1 3 4a1 1 0 0 1 1-1h3.5a1 1 0 0 1 1 1c0 1.25.2 2.45.57 3.57a1 1 0 0 1-.25 1z"/></svg>
        (323) 555 0148
      </li>
      <li>
        <svg viewBox="0 0 24 24" aria-hidden="true"><path d="M2 5h20v14H2z M3.5 6.5 12 13l8.5-6.5" fill="var(--yellow)" stroke="var(--card-dark)" stroke-width="1.5"/></svg>
        Marco@HarborlineNA.example
      </li>
    </ul>

    <address class="address" style="font-style:normal">
      782 n Alder Ave Suite 300 PMB2093<br>
      Los Angeles, CA 90013
    </address>

    <svg class="footer-band" viewBox="0 0 800 96" aria-hidden="true">
      <polygon points="0,30 360,30 340,52 0,52" fill="var(--grey-stripe)"/>
      <polygon points="0,52 340,52 380,34 800,34 800,96 0,96" fill="var(--yellow)"/>
    </svg>
    <p class="website">www.HarborlineNA.example</p>
  </section>

</body>
</html>
```